Business Card Design

Im looking for a business card that will market/promote myself as in independent/freelancer in the beauty industry. Im looking for something very modern, and clean looking. no specific colors just something that doesnt look cheesy, would like a very professional look

Industry/Entity Type

Business

Contact Information for Business Card

Corinne Balstrade, Hairstylist(Cut, color, blowdry, style, extensions, straightening treatments), makeup artist, red carpet, in-salon, editorial, tv, film, contact is 5307419863 cbglam@mailbrook.net, LA based

```html
<!DOCTYPE html>
<html lang="en">
<head>
<meta charset="utf-8">
<title>Corinne Balstrade — Business Card</title>
<link href="https://fonts.googleapis.com/css2?family=Archivo:wght@400;700;900&display=swap" rel="stylesheet">
<style>
  :root {
    --backdrop: #f0f0f0;
    --ink: #111111;
    --card-dark: #000000;
    --card-light: #ffffff;
    --paper-text: #222222;
    --shadow: rgba(0, 0, 0, 0.12);
  }
  * { margin: 0; padding: 0; box-sizing: border-box; }
  html, body {
    width: 1200px;
    height: 1000px;
    overflow: hidden;
    background: var(--backdrop);
  }
  .canvas {
    position: relative;
    width: 1200px;
    height: 1000px;
    background: var(--backdrop);
  }
  .card {
    position: absolute;
    top: 71px;
    height: 284px;
    box-shadow: 0 1px 6px var(--shadow);
  }
  .card-front {
    left: 91px;
    width: 486px;
    background: var(--card-dark);
    display: flex;
    align-items: center;
    justify-content: center;
    overflow: hidden;
  }
  .wordmark {
    font-family: "Archivo", Arial, sans-serif;
    font-weight: 700;
    font-size: 46px;
    letter-spacing: -0.5px;
    color: var(--card-light);
    white-space: nowrap;
  }
  .card-back {
    left: 618px;
    width: 489px;
    background: var(--card-light);
    text-align: center;
    font-family: "Archivo", Arial, sans-serif;
    color: var(--paper-text);
  }
  .holder-name {
    position: absolute;
    left: 0; right: 0;
    top: 86px;
    font-weight: 900;
    font-size: 17px;
    letter-spacing: 0.2px;
    color: var(--ink);
  }
  .holder-role {
    position: absolute;
    left: 0; right: 0;
    top: 108px;
    font-weight: 400;
    font-size: 13.5px;
    letter-spacing: 0.6px;
  }
  .contact-list {
    position: absolute;
    left: 0; right: 0;
    top: 145px;
    list-style: none;
    font-weight: 400;
    font-size: 13.5px;
    line-height: 21.5px;
    letter-spacing: 0.3px;
  }
</style>
</head>
<body>
  <main class="canvas">
    <section class="card card-front" aria-label="Business card front">
      <span class="wordmark">Corinne Balstrade</span>
    </section>
    <section class="card card-back" aria-label="Business card back">
      <h1 class="holder-name">CORINNE BALSTRADE</h1>
      <p class="holder-role">HAIR &amp; MAKEUP ARTIST</p>
      <ul class="contact-list">
        <li class="contact-phone">5307419863</li>
        <li class="contact-email">CBGLAM@MAILBROOK.NET</li>
        <li class="contact-location">LA BASED</li>
      </ul>
    </section>
  </main>
</body>
</html>
```